Brintell's Business Card

I need some designs for a new business card including the new logo attached. An old example of our business card is also attached to show all the data that should be included on the new design.
**I added some more examples someone had mocked up**

Contact Information for Business Card

Should include all info on other examples uploaded.

```html
<!DOCTYPE html>
<html lang="en">
<head>
<meta charset="utf-8">
<title>Brintell's Business Card</title>
<link rel="stylesheet" href="https://fonts.googleapis.com/css2?family=Fira+Sans:wght@400;600&family=Montserrat:wght@600&display=swap">
<style>
  :root {
    --bg: #e4e4e4;
    --card: #f4f4f4;
    --blue: #0b6db3;
    --red: #e42127;
    --ink: #2b2b2b;
    --white: #ffffff;
  }
  html, body { margin: 0; padding: 0; overflow: hidden; }
  body {
    width: 1200px; height: 960px;
    background: var(--bg);
    position: relative;
    font-family: "Fira Sans", Arial, sans-serif;
  }
  .card {
    position: absolute;
    left: 296px;
    width: 614px; height: 350px;
    background: var(--card);
    overflow: hidden;
  }
  .card--front { top: 107px; }
  .card--back { top: 511px; height: 351px; }
  .card svg.shapes { position: absolute; inset: 0; }

  .band-text {
    position: absolute; left: 0; right: 0;
    text-align: center; color: var(--white);
    font-weight: 600; margin: 0;
  }
  .badges { top: 22px; font-size: 20px; line-height: 27px; letter-spacing: 0.2px; }
  .service-area { top: 285px; font-size: 19px; line-height: 25px; }
  .service-area .cta { font-size: 17.5px; }

  .brand {
    position: absolute;
    display: flex; align-items: center; gap: 14px;
  }
  .brand-dot { border-radius: 50%; background: var(--red); flex: none; }
  .brand-name {
    font-family: "Montserrat", Arial, sans-serif;
    font-weight: 600; color: var(--blue);
    line-height: 1; margin: 0;
  }
  .card--front .brand { top: 150px; left: 0; right: 0; justify-content: center; }
  .card--front .brand-dot { width: 40px; height: 40px; }
  .card--front .brand-name { font-size: 54px; }
  .card--back .brand { top: 54px; left: 40px; }
  .card--back .brand-dot { width: 32px; height: 32px; }
  .card--back .brand-name { font-size: 42px; }

  .contact {
    position: absolute; right: 47px; top: 182px;
    text-align: right;
  }
  .contact .person { margin: 0; color: var(--blue); font-weight: 600; font-size: 21px; letter-spacing: 0.3px; }
  .contact .role { margin: 4px 0 0; color: var(--red); font-size: 17px; letter-spacing: 0.3px; }
  .contact .line {
    margin: 0; color: var(--ink); font-size: 17px; line-height: 25px;
    display: flex; justify-content: flex-end; align-items: center; gap: 4px;
  }
  .contact .lines { margin-top: 34px; }
  .contact .line svg { width: 16px; height: 16px; fill: var(--red); }
</style>
</head>
<body>

<section class="card card--front">
  <svg class="shapes" width="614" height="350" viewBox="0 0 614 350">
    <path d="M0,0 H614 V50 Q307,125 0,50 Z" fill="var(--blue)"/>
    <path d="M0,301 Q307,215 614,301 V350 H0 Z" fill="var(--red)"/>
  </svg>
  <p class="band-text badges">FAMILY OWNED &amp; OPERATED<br>LICENSED &amp; INSURED</p>
  <div class="brand">
    <span class="brand-dot"></span>
    <p class="brand-name">BRINTELL'S</p>
  </div>
  <p class="band-text service-area">Serves Maple Falls, IA &amp; Surrounding Areas<br><span class="cta">Call Today For All Your Hvac, Refrigeration &amp; Plumbing Needs</span></p>
</section>

<section class="card card--back">
  <svg class="shapes" width="614" height="351" viewBox="0 0 614 351">
    <path d="M0,0 H118 C66,60 52,110 66,160 C92,235 200,270 252,351 H0 Z" fill="var(--red)"/>
    <path d="M0,0 H106 C56,60 42,110 52,160 C70,225 150,270 205,351 H0 Z" fill="var(--blue)" stroke="var(--white)" stroke-width="3"/>
  </svg>
  <div class="brand">
    <span class="brand-dot"></span>
    <p class="brand-name">BRINTELL'S</p>
  </div>
  <div class="contact">
    <p class="person">DYLAN MARSH</p>
    <p class="role">CO-OWNER</p>
    <div class="lines">
      <p class="line">712.555.0147
        <svg viewBox="0 0 24 24" aria-hidden="true"><path d="M6.6 10.8c1.4 2.8 3.8 5.1 6.6 6.6l2.2-2.2c.3-.3.7-.4 1-.2 1.1.4 2.3.6 3.6.6.6 0 1 .4 1 1V20c0 .6-.4 1-1 1C10.6 21 3 13.4 3 4c0-.6.4-1 1-1h3.5c.6 0 1 .4 1 1 0 1.3.2 2.5.6 3.6.1.3 0 .7-.2 1z"/></svg>
      </p>
      <p class="line">service@brintellhvac.com
        <svg viewBox="0 0 24 24" aria-hidden="true"><path d="M2 5h20v14H2z M3.5 6.5 12 13l8.5-6.5" fill="var(--red)" stroke="var(--white)" stroke-width="1.5"/></svg>
      </p>
    </div>
  </div>
</section>

</body>
</html>
```